Four in One (Flexible infographic for Content Management Industry)

See attachment.
A graphic depicting 4 products, where each can stand on its own and each can be combined with others, but where, if all are taken together, the best result is achieved (the "super product").
Intended use is web. See attached file as an example.
The most basic idea is as the attached diagram shows, where 4 rectangles are arranged in a quadrangle, with a middle rectangle in the center representing the combined 4 products. This concept is fine except it is a bit too obvious as it stands. We are looking for either a variation of this or another concept.
The audience is technical + professional + enterprise - NOT consumers. Hence the design should be conservative in nature.
We are aware of tools like as Canva or Pictogram where such graphics are available, but we are looking for something with a bit more imagination and flexibility.
This graphic should be targeted to web sites and be delivered with vector-based (SVG) graphics.

```html
<!DOCTYPE html>
<html lang="en">
<head>
<meta charset="utf-8">
<title>Four in One – Super Product</title>
<link href="https://fonts.googleapis.com/css2?family=Plus+Jakarta+Sans:wght@700;800&family=Noto+Sans:wght@400;600&display=swap" rel="stylesheet">
<style>
  :root{
    --bg:#e8e8e8;
    --sheet:#ffffff;
    --purple:#8a15e6;
    --navy:#172a63;
    --navy-line:#3b4a78;
    --blue:#2e74e6;
    --teal:#22dcd0;
    --ink:#2e2e2e;
    --ring:#dedede;
    --pill:#efefef;
  }
  *{box-sizing:border-box;margin:0;padding:0}
  html,body{width:1200px;height:1200px;overflow:hidden;background:var(--bg)}
  .stage{position:relative;width:1200px;height:1200px}
  .sheet{position:absolute;left:110.6px;top:232.9px;width:978.7px;height:734px;background:var(--sheet)}
  .panel{position:absolute;width:446px;height:324.5px;border:1.4px solid;border-radius:20px}
  .panel--purple{left:140.4px;top:261.5px;border-color:var(--purple)}
  .panel--navy{left:615.5px;top:261.5px;border-color:var(--navy-line)}
  .panel--blue{left:140.4px;top:614.8px;border-color:var(--blue)}
  .panel--teal{left:615.5px;top:614.8px;border-color:var(--teal)}
  .wheel{position:absolute;left:0;top:0;width:1200px;height:1200px}
  .content{position:absolute;width:446px;height:324.5px}
  .content--purple{left:140.4px;top:261.5px}
  .content--navy{left:615.5px;top:261.5px}
  .content--blue{left:140.4px;top:614.8px}
  .content--teal{left:615.5px;top:614.8px}
  .content > *{position:absolute}
  .content--left > *{left:22.5px}
  .content--right > *{right:25px;text-align:right}
  .header{top:29px;font-family:"Plus Jakarta Sans",sans-serif;font-weight:800;font-size:18.4px;line-height:22px;letter-spacing:.1px;white-space:nowrap}
  .content--purple .header{color:var(--purple)}
  .content--navy .header{color:var(--navy)}
  .content--blue .header{color:var(--blue)}
  .content--teal .header{color:var(--teal)}
  .lead{top:55px;width:210px;font-family:"Noto Sans",sans-serif;font-size:12.6px;line-height:17.4px;color:var(--ink)}
  .bullets{top:138.7px;list-style:none}
  .bullets li{display:flex;align-items:center;gap:9px;height:25.8px;font-family:"Noto Sans",sans-serif;font-size:11.8px;letter-spacing:.5px;color:var(--ink);white-space:nowrap}
  .content--right .bullets li{flex-direction:row-reverse}
  .tick{width:15px;height:15px;flex:none}
  .content--purple .tick{color:var(--purple)}
  .content--navy .tick{color:var(--navy-line)}
  .content--blue .tick{color:var(--blue)}
  .content--teal .tick{color:var(--teal)}
  .learn-more{top:262px;width:157px;height:28px;border-radius:14px;background:var(--pill);color:var(--navy);font-family:"Plus Jakarta Sans",sans-serif;font-weight:700;font-size:11.4px;letter-spacing:2.6px;text-align:center!important;line-height:28px;text-decoration:none}
  .content--right .learn-more{right:24px}
  .core-label{font-family:"Plus Jakarta Sans",sans-serif;font-weight:800;font-size:28px;fill:var(--navy)}
</style>
</head>
<body>
<div class="stage">
  <div class="sheet"></div>

  <div class="panel panel--purple"></div>
  <div class="panel panel--navy"></div>
  <div class="panel panel--blue"></div>
  <div class="panel panel--teal"></div>

  <svg class="wheel" viewBox="0 0 1932 1932" aria-label="Four puzzle pieces forming the super product">
    <circle cx="966" cy="966" r="376" fill="#fff"/>
    <circle cx="966" cy="966" r="358" fill="none" stroke="var(--ring)" stroke-width="4"/>
    <circle cx="714" cy="714" r="16" fill="var(--purple)"/>
    <circle cx="1217" cy="714" r="16" fill="var(--navy)"/>
    <circle cx="714" cy="1217" r="16" fill="var(--blue)"/>
    <circle cx="1217" cy="1217" r="16" fill="var(--teal)"/>

    <g class="pieces">
      <path d="M966,966 L656,966 A310,310 0 0 1 966,656 Z" fill="var(--purple)"/>
      <path d="M966,966 L966,656 A310,310 0 0 1 1276,966 Z" fill="var(--navy)"/>
      <path d="M966,966 L1276,966 A310,310 0 0 1 966,1276 Z" fill="var(--teal)"/>
      <path d="M966,966 L966,1276 A310,310 0 0 1 656,966 Z" fill="var(--blue)"/>
      <path d="M966,650 V1282 M650,966 H1282" stroke="#fff" stroke-width="4"/>

      <path d="M956,734 L975,734 A34,34 0 1 1 975,772 L956,772 Z" fill="var(--purple)"/>
      <path d="M966,734 L975,734 A34,34 0 1 1 975,772 L966,772" fill="none" stroke="#fff" stroke-width="3"/>

      <path d="M731,976 L731,957 A34,34 0 1 1 769,957 L769,976 Z" fill="var(--blue)"/>
      <path d="M731,966 L731,957 A34,34 0 1 1 769,957 L769,966" fill="none" stroke="#fff" stroke-width="3"/>

      <path d="M1201,956 L1201,975 A34,34 0 1 1 1163,975 L1163,956 Z" fill="var(--navy)"/>
      <path d="M1201,966 L1201,975 A34,34 0 1 1 1163,975 L1163,966" fill="none" stroke="#fff" stroke-width="3"/>

      <path d="M956,1161 L975,1161 A34,34 0 1 1 975,1199 L956,1199 Z" fill="var(--blue)"/>
      <path d="M966,1161 L975,1161 A34,34 0 1 1 975,1199 L966,1199" fill="none" stroke="#fff" stroke-width="3"/>
    </g>

    <circle cx="966" cy="966" r="146" fill="#000" opacity=".12"/>
    <circle cx="966" cy="966" r="126" fill="#fff"/>

    <g class="icon-document" fill="#fff">
      <path d="M784,776 H820 A8,8 0 0 1 828,784 V818 L806,841 H784 A8,8 0 0 1 776,833 V784 A8,8 0 0 1 784,776 Z"/>
      <path d="M786,788 H816 M786,799 H816 M786,810 H804" stroke="var(--purple)" stroke-width="5" stroke-linecap="round"/>
      <path d="M808,840 L808,822 L826,822 Z" fill="var(--purple)"/>
    </g>

    <g class="icon-cloud">
      <path d="M1105,820 A16,16 0 0 1 1102,790 A24,24 0 0 1 1147,792 A14,14 0 0 1 1150,820 Z" fill="#fff"/>
      <circle cx="1146" cy="822" r="20" fill="#fff" stroke="var(--navy)" stroke-width="4"/>
      <path d="M1137,822 L1144,829 L1156,816" fill="none" stroke="var(--navy)" stroke-width="4" stroke-linecap="round" stroke-linejoin="round"/>
    </g>

    <g class="icon-apps" fill="#fff">
      <rect x="772" y="1094" width="27" height="27" rx="5"/>
      <rect x="772" y="1126" width="27" height="27" rx="5"/>
      <rect x="805" y="1126" width="27" height="27" rx="5"/>
      <rect x="806" y="1095" width="24" height="24" rx="5" transform="rotate(45 818 1107)"/>
    </g>

    <g class="icon-layers" fill="none" stroke="#fff" stroke-width="5" stroke-linejoin="round">
      <path d="M1129,1090 L1162,1108 L1129,1126 L1096,1108 Z" fill="#fff"/>
      <path d="M1096,1120 L1129,1138 L1162,1120"/>
      <path d="M1096,1132 L1129,1150 L1162,1132"/>
      <path d="M1116,1112 L1129,1104 L1142,1112" stroke="var(--teal)" stroke-width="4"/>
    </g>

    <g class="icon-idea" transform="translate(966 922)">
      <g fill="#1d4a66">
        <circle r="31"/>
        <rect x="-5" y="-39" width="10" height="12" rx="2"/>
        <rect x="-5" y="-39" width="10" height="12" rx="2" transform="rotate(45)"/>
        <rect x="-5" y="-39" width="10" height="12" rx="2" transform="rotate(90)"/>
        <rect x="-5" y="-39" width="10" height="12" rx="2" transform="rotate(135)"/>
        <rect x="-5" y="-39" width="10" height="12" rx="2" transform="rotate(180)"/>
        <rect x="-5" y="-39" width="10" height="12" rx="2" transform="rotate(225)"/>
        <rect x="-5" y="-39" width="10" height="12" rx="2" transform="rotate(270)"/>
        <rect x="-5" y="-39" width="10" height="12" rx="2" transform="rotate(315)"/>
      </g>
      <path d="M-10,16 A20,20 0 1 1 10,16 V22 H-10 Z" fill="#fff"/>
      <path d="M-4,20 V2 M4,20 V2 M-4,2 A4,4 0 1 1 -4,-2 M4,2 A4,4 0 1 0 4,-2" fill="none" stroke="#1d4a66" stroke-width="3"/>
      <rect x="-9" y="26" width="18" height="5" rx="2" fill="#1d4a66"/>
      <rect x="-6" y="34" width="12" height="4" rx="2" fill="#1d4a66"/>
    </g>

    <text class="core-label" x="966" y="1006" text-anchor="middle">SUPER</text>
    <text class="core-label" x="966" y="1038" text-anchor="middle">PRODUCT</text>
  </svg>

  <section class="content content--purple content--left">
    <h2 class="header">Header Text Here</h2>
    <p class="lead">Lorem ipsum dolor sit amet, consectetur adipiscing elit, sed do eiusmod tempor incididunt ut labore et dolore magna aliqua.</p>
    <ul class="bullets">
      <li><svg class="tick" viewBox="0 0 24 24"><circle cx="12" cy="12" r="10.5" fill="none" stroke="currentColor" stroke-width="1.6"/><path d="M7.5,12.2 L10.7,15.2 L16.5,9" fill="none" stroke="currentColor" stroke-width="1.6" stroke-linecap="round"/></svg>Insert bullet text here</li>
      <li><svg class="tick" viewBox="0 0 24 24"><circle cx="12" cy="12" r="10.5" fill="none" stroke="currentColor" stroke-width="1.6"/><path d="M7.5,12.2 L10.7,15.2 L16.5,9" fill="none" stroke="currentColor" stroke-width="1.6" stroke-linecap="round"/></svg>Insert bullet text here</li>
      <li><svg class="tick" viewBox="0 0 24 24"><circle cx="12" cy="12" r="10.5" fill="none" stroke="currentColor" stroke-width="1.6"/><path d="M7.5,12.2 L10.7,15.2 L16.5,9" fill="none" stroke="currentColor" stroke-width="1.6" stroke-linecap="round"/></svg>Insert bullet text here</li>
      <li><svg class="tick" viewBox="0 0 24 24"><circle cx="12" cy="12" r="10.5" fill="none" stroke="currentColor" stroke-width="1.6"/><path d="M7.5,12.2 L10.7,15.2 L16.5,9" fill="none" stroke="currentColor" stroke-width="1.6" stroke-linecap="round"/></svg>Insert bullet text here</li>
    </ul>
    <a class="learn-more" href="#">LEARN MORE</a>
  </section>

  <section class="content content--navy content--right">
    <h2 class="header">Header Text Here</h2>
    <p class="lead">Lorem ipsum dolor sit amet, consectetur adipiscing elit, sed do eiusmod tempor incididunt ut labore et dolore magna aliqua.</p>
    <ul class="bullets">
      <li><svg class="tick" viewBox="0 0 24 24"><circle cx="12" cy="12" r="10.5" fill="none" stroke="currentColor" stroke-width="1.6"/><path d="M7.5,12.2 L10.7,15.2 L16.5,9" fill="none" stroke="currentColor" stroke-width="1.6" stroke-linecap="round"/></svg>Insert bullet text here</li>
      <li><svg class="tick" viewBox="0 0 24 24"><circle cx="12" cy="12" r="10.5" fill="none" stroke="currentColor" stroke-width="1.6"/><path d="M7.5,12.2 L10.7,15.2 L16.5,9" fill="none" stroke="currentColor" stroke-width="1.6" stroke-linecap="round"/></svg>Insert bullet text here</li>
      <li><svg class="tick" viewBox="0 0 24 24"><circle cx="12" cy="12" r="10.5" fill="none" stroke="currentColor" stroke-width="1.6"/><path d="M7.5,12.2 L10.7,15.2 L16.5,9" fill="none" stroke="currentColor" stroke-width="1.6" stroke-linecap="round"/></svg>Insert bullet text here</li>
      <li><svg class="tick" viewBox="0 0 24 24"><circle cx="12" cy="12" r="10.5" fill="none" stroke="currentColor" stroke-width="1.6"/><path d="M7.5,12.2 L10.7,15.2 L16.5,9" fill="none" stroke="currentColor" stroke-width="1.6" stroke-linecap="round"/></svg>Insert bullet text here</li>
    </ul>
    <a class="learn-more" href="#">LEARN MORE</a>
  </section>

  <section class="content content--blue content--left">
    <h2 class="header">Header Text Here</h2>
    <p class="lead">Lorem ipsum dolor sit amet, consectetur adipiscing elit, sed do eiusmod tempor incididunt ut labore et dolore magna aliqua.</p>
    <ul class="bullets">
      <li><svg class="tick" viewBox="0 0 24 24"><circle cx="12" cy="12" r="10.5" fill="none" stroke="currentColor" stroke-width="1.6"/><path d="M7.5,12.2 L10.7,15.2 L16.5,9" fill="none" stroke="currentColor" stroke-width="1.6" stroke-linecap="round"/></svg>Insert bullet text here</li>
      <li><svg class="tick" viewBox="0 0 24 24"><circle cx="12" cy="12" r="10.5" fill="none" stroke="currentColor" stroke-width="1.6"/><path d="M7.5,12.2 L10.7,15.2 L16.5,9" fill="none" stroke="currentColor" stroke-width="1.6" stroke-linecap="round"/></svg>Insert bullet text here</li>
      <li><svg class="tick" viewBox="0 0 24 24"><circle cx="12" cy="12" r="10.5" fill="none" stroke="currentColor" stroke-width="1.6"/><path d="M7.5,12.2 L10.7,15.2 L16.5,9" fill="none" stroke="currentColor" stroke-width="1.6" stroke-linecap="round"/></svg>Insert bullet text here</li>
      <li><svg class="tick" viewBox="0 0 24 24"><circle cx="12" cy="12" r="10.5" fill="none" stroke="currentColor" stroke-width="1.6"/><path d="M7.5,12.2 L10.7,15.2 L16.5,9" fill="none" stroke="currentColor" stroke-width="1.6" stroke-linecap="round"/></svg>Insert bullet text here</li>
    </ul>
    <a class="learn-more" href="#">LEARN MORE</a>
  </section>

  <section class="content content--teal content--right">
    <h2 class="header">Header Text Here</h2>
    <p class="lead">Lorem ipsum dolor sit amet, consectetur adipiscing elit, sed do eiusmod tempor incididunt ut labore et dolore magna aliqua.</p>
    <ul class="bullets">
      <li><svg class="tick" viewBox="0 0 24 24"><circle cx="12" cy="12" r="10.5" fill="none" stroke="currentColor" stroke-width="1.6"/><path d="M7.5,12.2 L10.7,15.2 L16.5,9" fill="none" stroke="currentColor" stroke-width="1.6" stroke-linecap="round"/></svg>Insert bullet text here</li>
      <li><svg class="tick" viewBox="0 0 24 24"><circle cx="12" cy="12" r="10.5" fill="none" stroke="currentColor" stroke-width="1.6"/><path d="M7.5,12.2 L10.7,15.2 L16.5,9" fill="none" stroke="currentColor" stroke-width="1.6" stroke-linecap="round"/></svg>Insert bullet text here</li>
      <li><svg class="tick" viewBox="0 0 24 24"><circle cx="12" cy="12" r="10.5" fill="none" stroke="currentColor" stroke-width="1.6"/><path d="M7.5,12.2 L10.7,15.2 L16.5,9" fill="none" stroke="currentColor" stroke-width="1.6" stroke-linecap="round"/></svg>Insert bullet text here</li>
      <li><svg class="tick" viewBox="0 0 24 24"><circle cx="12" cy="12" r="10.5" fill="none" stroke="currentColor" stroke-width="1.6"/><path d="M7.5,12.2 L10.7,15.2 L16.5,9" fill="none" stroke="currentColor" stroke-width="1.6" stroke-linecap="round"/></svg>Insert bullet text here</li>
    </ul>
    <a class="learn-more" href="#">LEARN MORE</a>
  </section>
</div>
</body>
</html>
```